Last Minute Accommodation Booking Portal

AlpenGlowDeals.com needs a web platform to put potential clients in touch with available local ski resort accommodation. We are a dynamic, friendly and versatile company; we like a clean, graphic, contemporary look!

Hotel and apartment owners offer rooms to rent for certain dates with pricing; clients can ask for specific dates and number of beds with their budget. Offers can see searchers requests, searchers can only see offers.

All dates requested and offered must be within two weeks of the posting date and then posts should be removed when their arrival date has passed or they can be deleted by the person posting. We are envisaging that the hotels/apartments and customers would each need to register and login their offer/request.

Target Market(s)

28-55 years, active, high net worth but like a bargain, last mintue deciders, skiers and snowboarders or mountain enthusiasts, city folk wanting a winter break

Industry/Entity Type

Accommodation

Coding

Number of Pages Required

Font styles to use
Sans Serif

Colors
cee9f5
33a6d7
e34297
b768aa
ffffff

Requirements
Must have
• Efficient functionality so that many different parties - both offering deals and searching for deals - can search/list at the same time.
• option to translate to french
Nice to have
• opt in to 'alert/notification' when new offer or search is listed

```html
<!DOCTYPE html>
<html lang="en">
<head>
<meta charset="utf-8">
<title>AlpenGlowDeals.com – Last Minute Ski Stays</title>
<link href="https://fonts.googleapis.com/css2?family=Open+Sans:wght@400;600;700&display=swap" rel="stylesheet">
<style>
:root{
  --accent:#ef6461;
  --accent-dark:#d94f4c;
  --ink:#4a4a4a;
  --muted:#8a8a8a;
  --band:#f0f0f0;
  --white:#ffffff;
  --night:#1c1c1c;
  --snow:#cfd8e0;
}
*{box-sizing:border-box;margin:0;padding:0}
html,body{width:1200px;height:2504px;overflow:hidden}
body{font-family:"Open Sans",Arial,sans-serif;color:var(--ink);background:var(--white);position:relative}
.section{position:absolute;left:0;width:1200px}
.title{font-size:40px;font-weight:400;color:var(--accent);text-align:center}
.btn{display:inline-block;background:var(--accent);color:var(--white);font-size:14px;padding:8px 18px;border-radius:3px}
.copy{font-size:13px;line-height:20px;color:var(--muted)}

/* Hero */
.hero{top:0;height:488px;background:linear-gradient(180deg,#e9eef2 0%,#b9c5cf 30%,#6f7d88 60%,#3e4a52 100%)}
.hero-photo{position:absolute;inset:0}
.brand{position:absolute;top:14px;left:0;width:1200px;text-align:center;font-size:40px;font-weight:600;color:var(--accent)}
.nav{position:absolute;top:60px;left:0;width:1200px;display:flex;justify-content:center;gap:6px}
.nav span{font-size:14px;color:var(--ink);padding:4px 12px}
.nav .active{background:var(--accent);color:var(--white)}
.search{position:absolute;left:128px;top:384px;width:944px;height:88px;background:rgba(30,30,30,.6);display:flex;align-items:flex-end;padding:0 24px 16px;gap:36px}
.field label{display:block;color:var(--white);font-size:15px;margin-bottom:6px}
.field div{width:168px;height:26px;background:var(--white)}
.search .btn{margin-left:auto;padding:4px 22px}

/* Welcome */
.welcome{top:488px;height:452px}
.welcome .title{margin-top:28px}
.feature{position:absolute;width:520px}
.feature svg{position:absolute;left:0;top:4px}
.feature h3{margin-left:36px;font-size:26px;font-weight:400;color:var(--accent)}
.feature p{margin:6px 0 12px 36px;width:440px}
.feature .btn{margin-left:36px;padding:4px 16px;font-size:13px}

/* How it works */
.how{top:940px;height:240px;background:var(--band);text-align:center}
.how .title{margin-top:24px}
.how p{width:960px;margin:14px auto 22px}

/* News */
.news{top:1180px;height:228px}
.news .title{margin-top:24px}
.arrow{position:absolute;top:112px}
.post{position:absolute;top:94px;width:300px}
.date{position:absolute;left:0;top:0;width:76px;height:76px;border:3px solid var(--accent);border-radius:50%;text-align:center;color:var(--accent);padding-top:8px}
.date b{display:block;font-size:26px;line-height:28px;font-weight:600}
.date span{font-size:12px}
.post h4{margin-left:100px;font-size:13px;font-weight:600;color:var(--accent);text-transform:uppercase}
.post p{margin-left:100px;font-size:12px;line-height:18px;color:var(--ink)}

/* Testimonials */
.testimonials{top:1408px;height:392px;background:linear-gradient(90deg,#3a302a,#2a2523 40%,#2a2523 60%,#5b5550);text-align:center}
.testimonials .title{margin-top:24px;color:var(--white)}
.avatar{width:96px;height:96px;border-radius:50%;background:#b9a08c;border:4px solid var(--white);margin:22px auto 0}
.testimonials p{width:640px;margin:18px auto 10px;color:#ddd}
.testimonials .name{color:var(--accent);font-size:18px}

/* Gallery */
.gallery{top:1800px;height:400px}
.gallery .title{margin-top:8px}
.grid{position:absolute;left:208px;top:64px;width:892px;height:320px;display:grid;grid-template-columns:repeat(4,1fr);grid-template-rows:1fr 1fr;gap:6px}
.tile{width:100%;height:100%}

/* Subscribe */
.subscribe{top:2200px;height:220px;background:linear-gradient(90deg,#3d2f25,#2a2420 50%,#4a3d33);text-align:center}
.subscribe .title{margin-top:20px}
.subscribe p{width:800px;margin:10px auto 22px;color:#ddd}
.form{display:flex;justify-content:center;gap:10px}
.form div{width:300px;height:30px;background:var(--white)}
.form .btn{padding:5px 20px}

/* Footer */
.footer{top:2420px;height:84px;background:var(--night);text-align:center}
.footer nav{display:flex;justify-content:center;gap:40px;margin-top:18px}
.footer nav span{color:#ccc;font-size:14px}
.footer small{display:block;margin-top:16px;color:#999;font-size:11px}
</style>
</head>
<body>

<header class="section hero">
  <div class="hero-photo" role="img" aria-label="Snow-covered alpine ski village with chalets and mountains"></div>
  <div class="brand">AlpenGlowDeals.com</div>
  <nav class="nav"><span class="active">Home</span><span>About</span><span>Rooms</span><span>News</span><span>Contact</span></nav>
  <div class="search">
    <div class="field"><label>Select a City</label><div></div></div>
    <div class="field"><label>Check In</label><div></div></div>
    <div class="field"><label>Check Out</label><div></div></div>
    <div class="field"><label>Length of Night</label><div></div></div>
    <span class="btn">Search</span>
  </div>
</header>

<section class="section welcome">
  <h2 class="title">Welcome!</h2>
  <div class="feature" style="left:128px;top:112px">
    <svg width="24" height="28" viewBox="0 0 24 28"><rect x="2" y="2" width="18" height="24" fill="none" stroke="#444" stroke-width="2"/><path d="M6 9h10M6 14h10M6 19h6" stroke="#444" stroke-width="2"/></svg>
    <h3>Registration</h3>
    <p class="copy">Sign up in minutes as a guest or a host and start posting your requests or your free rooms for the next two weeks right away.</p>
    <span class="btn">Read More</span>
  </div>
  <div class="feature" style="left:640px;top:112px">
    <svg width="24" height="28" viewBox="0 0 24 28"><rect x="2" y="5" width="20" height="20" fill="none" stroke="#444" stroke-width="2"/><path d="M2 11h20M7 2v6M17 2v6" stroke="#444" stroke-width="2"/></svg>
    <h3>Book Late</h3>
    <p class="copy">Find great last minute stays close to the slopes, with fresh offers from hotels and apartments posted every single day.</p>
    <span class="btn">Read More</span>
  </div>
  <div class="feature" style="left:128px;top:292px">
    <svg width="24" height="28" viewBox="0 0 24 28"><path d="M4 14l6 6L21 6" fill="none" stroke="#444" stroke-width="3"/></svg>
    <h3>Be Choosy</h3>
    <p class="copy">Set your dates, number of beds and budget, then compare offers side by side and choose the stay that suits you best.</p>
    <span class="btn">Read More</span>
  </div>
  <div class="feature" style="left:640px;top:292px">
    <svg width="24" height="28" viewBox="0 0 24 28"><rect x="5" y="2" width="14" height="24" rx="2" fill="none" stroke="#444" stroke-width="2"/><circle cx="12" cy="22" r="1.5" fill="#444"/></svg>
    <h3>Go Mobile</h3>
    <p class="copy">Browse, post and book from your phone wherever you are, and get an alert the moment a new matching offer is listed.</p>
    <span class="btn">Read More</span>
  </div>
</section>

<section class="section how">
  <h2 class="title">How it works</h2>
  <p class="copy">Hosts list free rooms with dates and prices, guests post what they need with their budget. All dates fall within two weeks of posting, and each listing is removed once its arrival date has passed or when the owner deletes it. Register once, log in and start matching guests with rooms in the mountains today.</p>
  <span class="btn">Read More</span>
</section>

<section class="section news">
  <h2 class="title">News And Events</h2>
  <svg class="arrow" style="left:120px" width="16" height="24" viewBox="0 0 16 24"><path d="M12 3L4 12l8 9" fill="none" stroke="#ef6461" stroke-width="3"/></svg>
  <svg class="arrow" style="left:1064px" width="16" height="24" viewBox="0 0 16 24"><path d="M4 3l8 9-8 9" fill="none" stroke="#ef6461" stroke-width="3"/></svg>
  <article class="post" style="left:160px"><div class="date"><b>31</b><span>Dec</span></div><h4>Season Opens Now</h4><p>New lifts and pistes open this week, with fresh snow and plenty of late deals for skiers.</p></article>
  <article class="post" style="left:480px"><div class="date"><b>31</b><span>Dec</span></div><h4>New Year Party</h4><p>Celebrate on the slopes with music, fireworks and special offers from our partner hotels.</p></article>
  <article class="post" style="left:800px"><div class="date"><b>31</b><span>Dec</span></div><h4>Snow Weekend Deals</h4><p>Grab a weekend break in the mountains with rooms released by hosts at the last minute.</p></article>
</section>

<section class="section testimonials" role="img" aria-label="Dim chalet interiors and snowy balcony in the background">
  <h2 class="title">Testimonials</h2>
  <div class="avatar" role="img" aria-label="Portrait of a smiling guest"></div>
  <p class="copy">We booked a lovely apartment two days before arriving and paid far less than we expected. Simple to use, quick replies from the host and a great week of skiing.</p>
  <div class="name">Nora Wells</div>
</section>

<section class="section gallery">
  <h2 class="title">Gallery</h2>
  <div class="grid">
    <div class="tile" role="img" aria-label="Chalet terrace with mountain view" style="background:linear-gradient(#8fb4d4,#6a5444)"></div>
    <div class="tile" role="img" aria-label="Hotel room interior" style="background:linear-gradient(#a07a52,#5a3e28)"></div>
    <div class="tile" role="img" aria-label="Cosy lounge with fireplace" style="background:linear-gradient(#6b4a34,#2e2018)"></div>
    <div class="tile" role="img" aria-label="Snowy mountain peaks" style="background:linear-gradient(#9cc0e0,#e6eef4)"></div>
    <div class="tile" role="img" aria-label="Outdoor pool at resort" style="background:linear-gradient(#5aa9d6,#2c6f96)"></div>
    <div class="tile" role="img" aria-label="Spa pool lit at night" style="background:linear-gradient(#3ec0d0,#1a4e6a)"></div>
    <div class="tile" role="img" aria-label="Reception desk bell" style="background:linear-gradient(#c9b08a,#7a5a3a)"></div>
    <div class="tile" role="img" aria-label="Hotel staff welcoming a guest" style="background:linear-gradient(#d8d4cc,#6d6358)"></div>
  </div>
</section>

<section class="section subscribe" role="img" aria-label="Warm chalet interior in the background">
  <h2 class="title">Subscribe</h2>
  <p class="copy">Join our mailing list and be the first to hear about new rooms, fresh guest requests and special late offers across the resort every week.</p>
  <div class="form"><div></div><span class="btn">Submit</span></div>
</section>

<footer class="section footer">
  <nav><span>Home</span><span>About</span><span>Rooms</span><span>News</span><span>Contact</span></nav>
  <small>Copyright 2015. All Rights Reserved</small>
</footer>

</body>
</html>
```